Helicopter Company - Skyvane Sweden

I need a new design and implementation of a webpage. We rent helicopters and are also starting a school. We havre started a wordpress but the page is very ugly. Need a complete update. Logo exist already. We also have some pictures of helicotopers. We are open for all designs but it is important that it looks professionel, is eassy to update and will give an impression och structure and dicipline.
Updates

Target Market(s)

Customers that what to get a certificate to fly. It is expensive so it’s either people with a lot of money or people with a big dream. It is very serious business.

Industry/Entity Type

www.skyvane-demo.se

Coding

Coded - Design and coding required

Number of Pages Required

4 page

Font styles to use
Sans Serif

Colors
0054AA
0677BA
7BADD7
CADEEF
E8F1F8

Requirements
Must have
• A easy page the gives a feeling of seriousness and

```html
<!DOCTYPE html>
<html lang="sv">
<head>
<meta charset="utf-8">
<title>Skyvane – Hyr din helikopter</title>
<link href="https://fonts.googleapis.com/css2?family=Montserrat:wght@400;500;600;700&display=swap" rel="stylesheet">
<style>
  :root {
    --bg-dark: #181818;
    --bg-glow: #4a4a4a;
    --header-bg: #ffffff;
    --ink-dark: #1c1c1c;
    --ink-light: #ffffff;
    --accent: #0cc6f0;
    --card-bg: #333333;
  }
  * { box-sizing: border-box; margin: 0; padding: 0; }
  html, body { width: 1200px; height: 675px; overflow: hidden; }
  body {
    font-family: "Montserrat", sans-serif;
    background: var(--bg-dark);
    position: relative;
  }
  .page {
    position: absolute; inset: 0;
    background:
      radial-gradient(ellipse 380px 520px at -60px 80px, var(--bg-glow) 0%, rgba(40,40,40,0.6) 45%, transparent 80%),
      var(--bg-dark);
  }
  .site-header {
    position: absolute; left: 0; top: 20px; width: 1200px; height: 48px;
    background: var(--header-bg);
  }
  .brand {
    position: absolute; left: 72px; top: 12px;
    display: flex; align-items: center; gap: 8px;
    font-size: 21px; font-weight: 500; letter-spacing: 1px;
    color: var(--ink-dark);
  }
  .brand-mark { width: 14px; height: 14px; border-radius: 50%; background: var(--ink-dark); }
  .main-nav a {
    position: absolute; top: 15px;
    font-size: 13px; font-weight: 600; color: var(--ink-dark);
    text-decoration: none;
  }
  .lang svg { margin-left: 5px; vertical-align: 1px; }
  .btn {
    display: flex; align-items: center; justify-content: center;
    background: var(--accent); color: var(--ink-dark);
    border-radius: 18px; font-weight: 600; text-decoration: none;
  }
  .btn-faq {
    position: absolute; left: 993px; top: 7px; width: 135px; height: 35px;
    font-size: 13px;
  }
  .hero-visual {
    position: absolute; left: 400px; top: 110px; width: 800px; height: 320px;
    background: radial-gradient(ellipse 300px 150px at 420px 170px, #5a5a5a 0%, #2e2e2e 55%, transparent 100%);
  }
  .hero-copy { position: absolute; left: 59px; top: 232px; width: 400px; color: var(--ink-light); }
  .hero-copy h1 {
    font-size: 33px; font-weight: 700; line-height: 1.1; margin-bottom: 12px;
    white-space: nowrap;
  }
  .hero-copy p { font-size: 14.6px; font-weight: 500; line-height: 20.2px; white-space: nowrap; }
  .card {
    position: absolute; top: 503px; width: 336px; height: 146px;
    background: var(--card-bg); border-radius: 6px;
    padding: 16px 26px 0;
  }
  .card h2 {
    font-size: 17.5px; font-weight: 600; color: var(--accent); margin-bottom: 11px;
    white-space: nowrap;
  }
  .card p { font-size: 11.4px; line-height: 20px; color: var(--ink-light); font-weight: 500; white-space: nowrap; }
  .card .btn {
    position: absolute; left: 180px; top: 99px; width: 135px; height: 35px;
    font-size: 14.5px; font-weight: 500;
  }
  .card-1 { left: 69px; }
  .card-2 { left: 433px; }
  .card-3 { left: 797px; }
  .card-3 h2 { margin-left: 1px; }
</style>
</head>
<body>
<div class="page">
  <header class="site-header">
    <div class="brand"><span class="brand-mark"></span>SKYVANE</div>
    <nav class="main-nav">
      <a href="#" style="left:529px">Start</a>
      <a href="#" style="left:604px">Våra</a>
      <a href="#" style="left:676px">Hyra</a>
      <a href="#" style="left:749px">Jobb</a>
      <a href="#" style="left:825px">Om oss</a>
      <a href="#" class="lang" style="left:920px">ENG<svg width="8" height="5" viewBox="0 0 8 5"><path d="M1 1l3 3 3-3" fill="none" stroke="#1c1c1c" stroke-width="1.2"/></svg></a>
    </nav>
    <a href="#" class="btn btn-faq">Frågor?</a>
  </header>

  <div class="hero-visual" role="img" aria-label="Svart helikopter i studioljus mot mörk bakgrund"></div>

  <section class="hero-copy">
    <h1>HYR DIN HELIKOPTER!</h1>
    <p>Lorem ipsum dolor sit amet, consectetur adipiscing<br>elit, sed do eiusmod tempor incididunt ut labore et<br>dolore magna aliqua. Quis ipsum suspendisse ultrices<br>gravida. Risus commodo viverra maecenas accumsan<br>lacus vel facilisis.</p>
  </section>

  <article class="card card-1">
    <h2>Våra helikoptrar</h2>
    <p>Lorem ipsum dolor sit amet, consectetur adipi-<br>scing elit, sed do eiusmod tempor ...</p>
    <a href="#" class="btn">läsa mer</a>
  </article>
  <article class="card card-2">
    <h2>Hyra helikopter</h2>
    <p>Lorem ipsum dolor sit amet, consectetur adipi-<br>scing elit, sed do eiusmod tempor ...</p>
    <a href="#" class="btn">läsa mer</a>
  </article>
  <article class="card card-3">
    <h2>Andra typer av helikopterjobb</h2>
    <p>Lorem ipsum dolor sit amet, consectetur adipi-<br>scing elit, sed do eiusmod tempor ...</p>
    <a href="#" class="btn">läsa mer</a>
  </article>
</div>
</body>
</html>
```